Rebranding our business - Business Cards

We are currently rebranding our business and have just completed our new logo and now are wanting to have new business cards designed.

I will upload our old business card design as we would like to keep the same information on the card, Including the icon dot points on the back. I will also upload other designs I would like placed on the cards.. Such as a character,

I would like our power statement to be:
TKJ Removals -The Steady Haulers.

Instead of: Let TKJ Removals Carry Every Box Through Your Big Day,

I am happy for the designer to run with their own ideas.

```html
<!DOCTYPE html>
<html lang="en">
<head>
<meta charset="utf-8">
<title>TKJ Removals – Business Cards</title>
<link rel="stylesheet" href="https://fonts.googleapis.com/css2?family=Lato:wght@400;700&family=Arimo:wght@400&display=swap">
<style>
  :root {
    --navy: #1f3f86;
    --blue: #1d66b0;
    --blue-light: #2a78c2;
    --orange: #f16f2a;
    --orange-soft: #f5894a;
    --paper: #f4f4f4;
    --paper-shade: #dedede;
    --ink: #111111;
    --backdrop: #8d7360;
    --white: #ffffff;
  }
  * { margin: 0; padding: 0; box-sizing: border-box; }
  html, body { width: 1000px; height: 1200px; overflow: hidden; }
  body { background: var(--backdrop); position: relative; font-family: "Lato", Arial, sans-serif; }

  .card { position: absolute; left: 95px; width: 810px; height: 500px; overflow: hidden; box-shadow: 0 4px 10px rgba(0,0,0,.35); }
  .card--front { top: 78px; background: radial-gradient(ellipse at 45% 85%, var(--white) 0%, var(--paper) 40%, var(--paper-shade) 100%); }
  .card--back { top: 625px; background: radial-gradient(ellipse at 55% 35%, var(--white) 0%, var(--paper) 45%, var(--paper-shade) 100%); }

  .abs { position: absolute; }

  /* front */
  .front-sky { left: 0; top: 0; width: 810px; height: 275px; background: linear-gradient(90deg, var(--navy) 0%, var(--blue) 60%, var(--blue-light) 100%); }
  .brand-name { font-family: "Lato", Arial, sans-serif; font-weight: 700; white-space: nowrap; line-height: 1; }
  .front-brand { left: 43px; top: 110px; font-size: 54px; color: var(--white); }
  .power-band { left: 0; top: 275px; width: 810px; height: 44px; background: var(--orange); }
  .power-text { left: 42px; top: 285px; font-family: "Arimo", sans-serif; font-size: 21px; color: var(--white); }
  .mascot { left: 505px; top: 40px; width: 300px; height: 372px; border-radius: 8px;
    background: linear-gradient(180deg, rgba(241,111,42,.85) 0%, rgba(60,60,60,.85) 55%, rgba(200,200,200,.7) 100%); }
  .parcel { left: 420px; top: 324px; width: 98px; height: 74px; border-radius: 4px; background: linear-gradient(180deg, #f3a455, #e3893a); }
  .owner-name { left: 43px; top: 326px; font-size: 22px; color: var(--ink); }
  .owner-role { left: 43px; top: 353px; font-size: 17px; color: var(--orange); }
  .contact-list { list-style: none; font-size: 19px; color: var(--ink); }
  .contact-list li { display: flex; align-items: center; height: 24.7px; }
  .contact-list svg { width: 17px; height: 17px; margin-right: 8px; flex: none; }
  .front-contacts { left: 43px; top: 381px; }
  .front-web { left: 434px; top: 427px; }

  /* back */
  .back-brand { left: 40px; top: 88px; font-size: 56px; color: var(--blue); }
  .offer { left: 485px; top: 68px; font-size: 20px; color: var(--ink); }
  .back-contacts { left: 485px; top: 103px; font-size: 20px; }
  .back-contacts li { height: 27px; }
  .provides-band { left: 0; top: 257px; width: 810px; height: 46px; background: linear-gradient(90deg, var(--navy), var(--blue)); }
  .provides-title { left: 40px; top: 268px; font-size: 19px; color: var(--white); letter-spacing: .3px; }
  .services-band { left: 0; top: 306px; width: 810px; height: 194px; background: linear-gradient(90deg, var(--orange) 0%, var(--orange-soft) 100%); }
  .service-list { left: 37px; top: 325px; list-style: none; font-family: "Arimo", sans-serif; font-size: 19px; color: var(--white); }
  .service-list li { display: flex; align-items: center; height: 30.5px; }
  .service-list svg { width: 19px; height: 19px; margin-right: 11px; flex: none; }
  .box-art { left: 560px; top: 320px; width: 170px; height: 158px; border-radius: 6px; background: linear-gradient(160deg, rgba(255,255,255,.9), rgba(255,255,255,.65)); }
</style>
</head>
<body>

<section class="card card--front">
  <div class="abs front-sky"></div>
  <div class="abs brand-name front-brand">TKJ Removals</div>
  <div class="abs power-band"></div>
  <div class="abs power-text">TKJ Removals -The Steady Haulers.</div>
  <div class="abs mascot" role="img" aria-label="Cartoon removalist in orange shirt and cap giving a thumbs up, leaning on a hand trolley"></div>
  <div class="abs parcel" role="img" aria-label="Cardboard box marked fragile"></div>

  <div class="abs owner-name">Marcus Delaney</div>
  <div class="abs owner-role">Owner Operator</div>

  <ul class="abs contact-list front-contacts">
    <li><svg viewBox="0 0 16 16"><rect width="16" height="16" rx="2" fill="var(--navy)"/><rect x="5" y="2.5" width="6" height="11" rx="1" fill="none" stroke="#fff" stroke-width="1.3"/></svg>0400 318 762</li>
    <li><svg viewBox="0 0 16 16"><rect width="16" height="16" rx="2" fill="var(--navy)"/><path d="M3 7 Q8 2 13 7 L11 8.5 L10 7 H6 L5 8.5 Z M4.5 9.5 H11.5 L12 13 H4 Z" fill="#fff"/></svg>07 5550 2846</li>
    <li><svg viewBox="0 0 16 16"><rect width="16" height="16" rx="2" fill="var(--navy)"/><path d="M8 2.5 A3.8 3.8 0 0 1 11.8 6.3 C11.8 9 8 13.5 8 13.5 C8 13.5 4.2 9 4.2 6.3 A3.8 3.8 0 0 1 8 2.5 Z" fill="none" stroke="#fff" stroke-width="1.3"/><circle cx="8" cy="6.3" r="1.3" fill="#fff"/></svg>Sunvale,QLD 4000</li>
    <li><svg viewBox="0 0 16 16"><rect width="16" height="16" rx="2" fill="var(--navy)"/><rect x="3" y="4.5" width="10" height="7" fill="none" stroke="#fff" stroke-width="1.2"/><path d="M3 4.5 L8 9 L13 4.5" fill="none" stroke="#fff" stroke-width="1.2"/></svg>tkjremovals@haulmail.com</li>
  </ul>

  <ul class="abs contact-list front-web">
    <li><svg viewBox="0 0 16 16"><rect width="16" height="16" rx="2" fill="var(--navy)"/><circle cx="8" cy="8" r="4.8" fill="none" stroke="#fff" stroke-width="1.2"/><path d="M3.2 8 H12.8 M8 3.2 V12.8" stroke="#fff" stroke-width="1"/></svg>www.tkjremovals.com.au</li>
    <li><svg viewBox="0 0 16 16"><rect width="16" height="16" rx="2" fill="var(--navy)"/></svg>www.friendpage.com/tkjremovals</li>
  </ul>
</section>

<section class="card card--back">
  <div class="abs brand-name back-brand">TKJ Removals</div>

  <div class="abs offer">FREE TRANSIT INSURANCE!</div>
  <ul class="abs contact-list back-contacts">
    <li><svg viewBox="0 0 16 16"><rect width="16" height="16" rx="2" fill="var(--orange)"/><rect x="5" y="2.5" width="6" height="11" rx="1" fill="none" stroke="#fff" stroke-width="1.3"/></svg>0400 318 762</li>
    <li><svg viewBox="0 0 16 16"><rect width="16" height="16" rx="2" fill="var(--orange)"/><path d="M3 7 Q8 2 13 7 L11 8.5 L10 7 H6 L5 8.5 Z M4.5 9.5 H11.5 L12 13 H4 Z" fill="#fff"/></svg>07 5550 2846</li>
    <li><svg viewBox="0 0 16 16"><rect width="16" height="16" rx="2" fill="var(--orange)"/><rect x="3" y="4.5" width="10" height="7" fill="none" stroke="#fff" stroke-width="1.2"/><path d="M3 4.5 L8 9 L13 4.5" fill="none" stroke="#fff" stroke-width="1.2"/></svg>tkjremovals@haulmail.com</li>
    <li><svg viewBox="0 0 16 16"><rect width="16" height="16" rx="2" fill="var(--orange)"/><circle cx="8" cy="8" r="4.8" fill="none" stroke="#fff" stroke-width="1.2"/><path d="M3.2 8 H12.8 M8 3.2 V12.8" stroke="#fff" stroke-width="1"/></svg>www.tkjremovals.com.au</li>
  </ul>

  <div class="abs provides-band"></div>
  <div class="abs provides-title">TKJ REMOVALS PROVIDES :</div>
  <div class="abs services-band"></div>

  <ul class="abs service-list">
    <li><svg viewBox="0 0 20 20"><rect x="2" y="4" width="11" height="9" fill="#fff"/><path d="M13 7 H16 L18 10 V13 H13 Z" fill="#fff"/><circle cx="6" cy="15" r="2" fill="#fff"/><circle cx="15" cy="15" r="2" fill="#fff"/></svg>Local, Country &amp; Interstate Removals</li>
    <li><svg viewBox="0 0 20 20"><path d="M10 2 L19 10 H16 V18 H12 V13 H8 V18 H4 V10 H1 Z" fill="#fff"/></svg>Home &amp; Hi Rise Removals</li>
    <li><svg viewBox="0 0 20 20"><path d="M2 4 L6 4 L11 14" fill="none" stroke="#fff" stroke-width="2"/><circle cx="12" cy="16" r="2.2" fill="#fff"/><rect x="9" y="5" width="8" height="7" transform="rotate(-25 13 8)" fill="#fff"/></svg>Office &amp; Factory Relocation’s</li>
    <li><svg viewBox="0 0 20 20"><path d="M5 2 H15 V8 A5 5 0 0 1 5 8 Z" fill="#fff"/><rect x="9" y="12" width="2" height="5" fill="#fff"/><rect x="6" y="17" width="8" height="2" fill="#fff"/></svg>Pre - Packing &amp; Unpaking Service’s</li>
    <li><svg viewBox="0 0 20 20"><rect x="7" y="2" width="9" height="8" fill="#fff"/><path d="M1 13 H7 L11 15 H17 L17 17 H9 L1 17 Z" fill="#fff"/></svg>Storage Solution</li>
  </ul>

  <div class="abs box-art" role="img" aria-label="White outline illustration of an open cardboard moving box"></div>
</section>

</body>
</html>
```